Agriculture Business Card

I want to use my existing logo and use my tagline of "Don't Guess...Soil Test" on the card. Looking for a double sided card that will really get peoples attention.
Contact Info:
Brisco Harvest Crop Solutions
Calvin Brisco
2917 K Lane
Fallow Creek, KS 68539
402-815-2493
calvin.r.brisco@furrowpost.net

```html
<!DOCTYPE html>
<html lang="en">
<head>
<meta charset="utf-8">
<title>Brisco Harvest Crop Solutions – Business Card</title>
<link href="https://fonts.googleapis.com/css2?family=Montserrat:wght@400;500;600&display=swap" rel="stylesheet">
<style>
  :root {
    --backdrop: #2b2a29;
    --card-white: #ffffff;
    --soil-brown: #a0674e;
    --deep-brown: #7a4a36;
    --leaf-green: #34a843;
    --corn-gold: #f4ae1a;
    --text-grey: #555555;
  }
  * { margin: 0; padding: 0; box-sizing: border-box; }
  html, body { width: 1200px; height: 900px; overflow: hidden; }
  body {
    background: var(--backdrop);
    font-family: "Montserrat", sans-serif;
    position: relative;
  }
  .card {
    position: absolute;
    left: 250px;
    width: 700px;
    height: 400px;
    overflow: hidden;
    box-shadow: 0 10px 30px rgba(0,0,0,0.45);
  }
  .card--front { top: 40px; background: var(--card-white); }
  .card--back { top: 460px; background: var(--soil-brown); }

  .front-waves { position: absolute; inset: 0; }

  .brand {
    position: absolute;
    left: 50px;
    top: 110px;
    width: 240px;
    display: flex;
    align-items: center;
    gap: 14px;
  }
  .brand__dot {
    flex: none;
    width: 22px;
    height: 22px;
    border-radius: 50%;
    background: var(--corn-gold);
  }
  .brand__name {
    font-weight: 600;
    font-size: 26px;
    line-height: 1.15;
    color: var(--deep-brown);
  }

  .divider {
    position: absolute;
    left: 320px;
    top: 70px;
    width: 1px;
    height: 220px;
    background: var(--soil-brown);
  }

  .contact {
    position: absolute;
    left: 360px;
    top: 92px;
  }
  .contact__name {
    font-weight: 600;
    font-size: 28px;
    letter-spacing: 0.5px;
    text-transform: uppercase;
    color: var(--leaf-green);
    margin-bottom: 18px;
  }
  .contact__address {
    font-size: 17px;
    line-height: 1.4;
    color: var(--text-grey);
    margin-bottom: 14px;
  }
  .contact__line {
    display: flex;
    align-items: center;
    gap: 8px;
    font-size: 17px;
    line-height: 1.5;
    color: var(--text-grey);
  }
  .contact__icon { width: 14px; height: 14px; flex: none; }

  .back-mark {
    position: absolute;
    left: 50%;
    top: 120px;
    transform: translateX(-50%);
    display: flex;
    align-items: center;
    gap: 14px;
  }
  .back-mark__dot {
    width: 22px;
    height: 22px;
    border-radius: 50%;
    background: var(--deep-brown);
  }
  .back-mark__name {
    font-weight: 600;
    font-size: 30px;
    color: var(--deep-brown);
    white-space: nowrap;
  }
  .tagline {
    position: absolute;
    left: 0;
    right: 0;
    bottom: 70px;
    text-align: center;
    font-size: 24px;
    font-weight: 500;
    letter-spacing: 0.5px;
    color: var(--corn-gold);
  }
</style>
</head>
<body>

<section class="card card--front" aria-label="Card front">
  <svg class="front-waves" viewBox="0 0 700 400" width="700" height="400" aria-hidden="true">
    <path d="M0,300 Q150,315 250,400 L0,400 Z" fill="var(--soil-brown)"/>
    <path d="M0,290 Q160,306 264,400" fill="none" stroke="var(--leaf-green)" stroke-width="5"/>
    <path d="M440,400 Q590,382 700,340 L700,400 Z" fill="var(--soil-brown)"/>
    <path d="M430,392 Q590,372 700,328" fill="none" stroke="var(--corn-gold)" stroke-width="5"/>
  </svg>

  <div class="brand">
    <span class="brand__dot"></span>
    <span class="brand__name">Brisco Harvest Crop Solutions</span>
  </div>

  <div class="divider"></div>

  <div class="contact">
    <h1 class="contact__name">Calvin Brisco</h1>
    <p class="contact__address">2917 K Lane<br>Fallow Creek, KS 68539</p>
    <p class="contact__line">
      <svg class="contact__icon" viewBox="0 0 24 24" aria-hidden="true"><path fill="var(--corn-gold)" d="M6.6 10.8a15.1 15.1 0 0 0 6.6 6.6l2.2-2.2a1 1 0 0 1 1-.25 11.4 11.4 0 0 0 3.6.57 1 1 0 0 1 1 1V20a1 1 0 0 1-1 1A17 17 0 0 1 3 4a1 1 0 0 1 1-1h3.5a1 1 0 0 1 1 1c0 1.25.2 2.45.57 3.57a1 1 0 0 1-.25 1z"/></svg>
      402-815-2493
    </p>
    <p class="contact__line">
      <svg class="contact__icon" viewBox="0 0 24 24" aria-hidden="true"><path fill="var(--corn-gold)" d="M2 5h20v14H2z"/><path fill="none" stroke="#fff" stroke-width="1.8" d="M2 5l10 8 10-8"/></svg>
      calvin.r.brisco@furrowpost.net
    </p>
  </div>
</section>

<section class="card card--back" aria-label="Card back">
  <div class="back-mark">
    <span class="back-mark__dot"></span>
    <span class="back-mark__name">Brisco Harvest Crop Solutions</span>
  </div>
  <p class="tagline">Don't Guess...Soil Test</p>
</section>

</body>
</html>
```